"Show Times" Poster for Stunt Show

I need a fairly simple 24"x 36" poster made. I'm a professional mountain bike stunt rider and I need a poster to put on a sandwich board to display my showtimes for people walking by. The top of the poster will say: Mountain Bike (Trials) Stunt Show This text will be centered at the top BUT I want the "(Trials)" to be slightly crooked and a bit opaque with a stamped-looking font and overlap the other words just slightly. Hopefully that makes sense. Somewhere in the middle will be a photoshopped picture of me doing a stunt on my bike. The bottom will have a blank white space titled, "Show Times:" that I can write my showtimes inside of. I've attached a wildly crude and poor drawing of the basic concept. Remember, this is for a stunt show so it must look cool and have some rad colors and design... but also be simple. I will provide a picture of myself riding to be used in the poster. It will take up the middle third.

Target Market(s)

Families, Parents, Kids, general public, mountain bike enthusiastss

Industry/Entity Type

Entertainment Industry

Font styles to use
Sans Serif

Colors

Designer to choose colors to be used in the design.

Requirements
Must have
• A blank, rectangular, white space on the bottom for Show times Labelled "Show Times:"
Nice to have
• I'd like background of the whole poster to be relatively black with cool subtle graphics.

```html
<!DOCTYPE html>
<html lang="en">
<head>
<meta charset="utf-8">
<title>Mountain Bike Stunt Show – Show Time Poster</title>
<link rel="stylesheet" href="https://fonts.googleapis.com/css2?family=Black+Ops+One&family=Oswald:wght@500;700&display=swap">
<style>
  :root {
    --stage: #d9d9d9;
    --poster-black: #1f1b1c;
    --title-red: #c9262c;
    --paper: #ffffff;
    --tag-ink: #e8e4e5;
    --text-dark: #151515;
  }
  * { margin: 0; padding: 0; box-sizing: border-box; }
  html, body {
    width: 1200px;
    height: 1200px;
    overflow: hidden;
    background: var(--stage);
  }
  .poster {
    position: absolute;
    left: 220px;
    top: 50px;
    width: 760px;
    height: 1100px;
    background: var(--poster-black);
    overflow: hidden;
  }
  .poster-title {
    position: absolute;
    left: 90px;
    top: 50px;
    font-family: "Black Ops One", "Arial Black", sans-serif;
    font-weight: 400;
    font-size: 56px;
    line-height: 64px;
    color: var(--title-red);
    letter-spacing: 1px;
    text-transform: uppercase;
  }
  .poster-title span { display: block; }
  .trial-tag {
    position: absolute;
    left: 545px;
    top: 122px;
    font-family: "Black Ops One", "Arial Black", sans-serif;
    font-weight: 400;
    font-size: 46px;
    line-height: 1;
    letter-spacing: 3px;
    color: var(--tag-ink);
    opacity: 0.85;
    transform: rotate(-9deg);
    transform-origin: left center;
  }
  .rider-art {
    position: absolute;
    left: 80px;
    top: 190px;
    width: 620px;
    height: 560px;
  }
  .film-holes {
    position: absolute;
    left: 0;
    width: 100%;
    height: 14px;
    background: repeating-linear-gradient(90deg,
      var(--paper) 0 14px, transparent 14px 23px);
    background-position: 10px 0;
  }
  .film-holes.top { top: 779px; }
  .film-holes.bottom { top: 1049px; }
  .showtimes-board {
    position: absolute;
    left: 0;
    top: 803px;
    width: 100%;
    height: 232px;
    background: var(--paper);
  }
  .showtimes-label {
    display: block;
    margin-top: 22px;
    text-align: center;
    font-family: "Oswald", "Arial Narrow", sans-serif;
    font-weight: 700;
    font-size: 40px;
    line-height: 1;
    color: var(--text-dark);
    letter-spacing: 0.5px;
  }
</style>
</head>
<body>
  <main class="poster">
    <h1 class="poster-title">
      <span>Mountain Bike</span>
      <span>Stunt Show</span>
    </h1>
    <p class="trial-tag">TRIAL</p>

    <svg class="rider-art" viewBox="0 0 620 560" role="img"
         aria-label="Photo of the rider performing a trials stunt on a mountain bike in an indoor arena">
      <defs>
        <linearGradient id="photoTone" x1="0" y1="0" x2="1" y2="1">
          <stop offset="0" stop-color="#d8d4d6"/>
          <stop offset="0.45" stop-color="#a89ea5"/>
          <stop offset="0.75" stop-color="#b98a9c"/>
          <stop offset="1" stop-color="#e6e2e4"/>
        </linearGradient>
      </defs>
      <path d="M70 140 L180 60 L330 20 L460 40 L560 90 L590 200 L570 330 L560 460 L470 520 L300 535 L140 530 L60 460 L40 330 L50 220 Z"
            fill="url(#photoTone)"/>
      <g fill="var(--paper)">
        <circle cx="40" cy="120" r="9"/>
        <circle cx="22" cy="160" r="6"/>
        <circle cx="58" cy="300" r="7"/>
        <circle cx="26" cy="410" r="5"/>
        <circle cx="590" cy="80" r="8"/>
        <circle cx="612" cy="170" r="6"/>
        <circle cx="600" cy="420" r="10"/>
        <circle cx="100" cy="535" r="9"/>
        <circle cx="160" cy="550" r="6"/>
        <circle cx="310" cy="14" r="11"/>
      </g>
      <g stroke="var(--paper)" stroke-width="7" stroke-linecap="round">
        <line x1="50" y1="90" x2="170" y2="30"/>
        <line x1="430" y1="550" x2="590" y2="480"/>
      </g>
    </svg>

    <div class="film-holes top"></div>
    <section class="showtimes-board">
      <h2 class="showtimes-label">SHOW TIME</h2>
    </section>
    <div class="film-holes bottom"></div>
  </main>
</body>
</html>
```